Alcohol Marketing website

Home page and information page design, details as follows

CLIENT PURPOSE
Increase online visibility and create good contacts to increase business.

SERVICES
Drinks Marketing Consultancy
Brand Representation
Spirit Brand Sales & Marketing
Brand Development
Brand Distribution
Brand Launch & Introductions

COMPETITION
merrycasks.co.uk -
talvoranbrands.co.uk -

WEBSITE(S) CLIENT LIKES
Small competitors I admire:
http://www.merrycasks.co.uk/main.htm
http://www.talvoranbrands.com
http://www.vaultpicks.co.uk/spiritsliqueursbybrand.php
http://www.quellomarks.com/page1.html
http://www.zirnopaxtra.co.uk/index.asp

Nice page layout:
http://www.kvworks.com/
http://www.dmhallies.com/
http://www.pelvik.com/index.cfm?do=pelvik.home

WEBSITE CLIENT DOES NOT LIKE
http://www.tidemarque.com/
http://www.parlour-labels.com/
http://www.yonderpours.co.uk/aboutUs.html
http://www.graincorkhouse.com/
http://www.orbitmarques.co.uk/default.asp
http://www.summit-labels.co.uk/start.htm
http://www.durlay.co.uk/
http://www.pkcasks.com/default2.aspx
http://www.quaff-marques.co.uk/mainpage.aspx

COMPANY LOGO
Customer has a company logo (Supplied)

COLOURS:
Blue
White

STRAPLINE:
No

WEBSITE THEME: Marketing

IMAGES THAT BEST REFLECT THE COMPANY:
Spirits / Drinks

HEADER IMAGE:
Spirits / Brands

PAGES:
home
strength& flavour
a little about us
our spirit marketing
big brand success
speak to us

USER JOURNEYS:
General Service > Land on website >Navigation > Info Pages > Contact Form
Questions > Land on website > Message Banners > Info Pages > Contact Form
Contact > Land on website > Clear Telephone / Email Banner > Contact Form

CALL TO ACTION BANNER:
If you need help making your drink the next big brand, speak to us today.

KEYWORDS THAT RELATE TO THE BUSINESS:
brand marketing
drinks marketing
spirits marketing
brand marketing strategy
alcoholic drinks marketing
Drinks Brand Development

LOCATION(S):
United Kingdom -
Worldwide -

Target Market(s)

Male & Female
30-60
Marketing Directors
Brand Developers
Export Directors
Brand Managers

Industry/Entity Type

Marketing

Number of Pages Required

2 pages

Requirements
Must have
• This design will be integrated into wordpress, I have attached a wireframe of what we need, this is NOT a strict guide but contains content that is essential, the wireframes shows the priority of statements and products. the images supplied need to sell the products and services.
The main banner will eventually be animated so this needs to be taken into account.
The cliemt has supplied images which will need to be used in the design , however if you feel you have better images in the same style then they can be used.
Nice to have
• animation included, Jquery
Should not have
• NO fully flash sites or designs, this site will be Search engine optimised and updateable

```html
<!DOCTYPE html>
<html lang="en">
<head>
<meta charset="utf-8">
<title>Grain &amp; Glint – home and about pages</title>
<link rel="stylesheet" href="https://fonts.googleapis.com/css2?family=Arimo:wght@400;700&family=Open+Sans:wght@400;600&display=swap">
<style>
:root{
  --blue:#1aa6d8;
  --blue-dark:#0f8fc0;
  --ink:#3c3c3c;
  --nav-ink:#4a4a4a;
  --page-bg:#e6e6e6;
  --panel-bg:#ececec;
  --card-bg:#fbfbfb;
  --rule:#c9c9c9;
  --yellow:#f4e61c;
}
*{box-sizing:border-box;margin:0;padding:0}
html,body{width:1200px;height:581px;overflow:hidden;background:#fff}
body{position:relative;font-family:"Arimo",Arial,sans-serif;color:var(--ink)}

.page{position:absolute;top:21px;width:567px;background:linear-gradient(#ececec,#e2e2e2)}
.page--home{left:21px;height:426px}
.page--about{left:610px;height:543px}

.brand{position:absolute;left:30px;top:16px;display:flex;align-items:center;gap:4px;
  font-family:"Arimo",Arial,sans-serif;font-size:9px;color:var(--blue)}
.brand__dot{width:8px;height:8px;border-radius:50%;background:var(--blue)}

.social{position:absolute;left:435px;top:0;width:111px;height:21px;background:#f3f3f3;
  border:1px solid #d8d8d8;border-top:0;border-radius:0 0 4px 4px;display:flex;
  align-items:center;justify-content:space-around;padding:0 6px;font-size:5.5px}
.social a{color:#666;text-decoration:underline;display:flex;align-items:center;gap:3px}
.social__box{width:9px;height:9px;background:var(--blue);border-radius:2px}

.contact{position:absolute;right:23px;top:29px;text-align:right;font-size:7px;line-height:10px;color:#444}
.contact b{font-weight:400;color:var(--blue)}

.nav{position:absolute;left:23px;top:68px;width:521px;height:38px;list-style:none}
.nav li{position:absolute;top:0;font-size:12.5px;line-height:12px;color:var(--nav-ink)}
.nav li.is-active{color:var(--blue)}
.nav .divider{position:absolute;top:4px;width:1px;height:20px;background:#cfcfcf}
.nav__bar{position:absolute;left:0;top:34px;width:521px;height:4px;background:#fff}
.nav__bar span{position:absolute;top:0;height:4px;background:var(--blue)}

.hero{position:absolute;left:23px;top:106px;width:521px;height:151px;
  background:linear-gradient(90deg,#2d3a44 0%,#52606a 28%,#3a3f41 45%,#b7771d 58%,#e39a2a 72%,#d9a338 100%)}
.hero__quote{position:absolute;left:306px;top:18px;width:215px;height:114px;background:rgba(20,170,220,.88);
  text-align:right;padding:18px 9px 0 0;font-family:"Open Sans",sans-serif;color:#fff}
.hero__quote p{font-size:17.5px;line-height:17px;letter-spacing:1.4px}
.hero__quote cite{display:block;margin-top:16px;font-style:normal;font-size:6.5px;line-height:7px;color:var(--yellow);font-weight:700}

.features{position:absolute;left:23px;width:521px;background:var(--panel-bg)}
.page--home .features{top:257px;height:122px}
.page--about .features{top:386px;height:117px}
.card{position:absolute;top:10px;width:159px;height:103px;background:var(--card-bg);border:1px solid #dedede;border-radius:3px;padding:10px 9px 0}
.card h3{font-family:"Open Sans",sans-serif;font-weight:400;font-size:10.5px;line-height:13px;color:var(--blue);letter-spacing:.3px}
.card hr{border:0;height:1px;background:linear-gradient(90deg,transparent,#d6d6d6,transparent);margin:9px 0 8px}
.card p{font-size:6px;line-height:9.6px;letter-spacing:.2px;color:#333}
.card a{display:flex;align-items:center;gap:4px;margin-top:3px;font-size:5.5px;color:var(--blue)}
.card a svg{width:8px;height:8px}

.footer{position:absolute;left:0;width:567px;text-align:center;font-size:5px}
.footer .links{color:var(--blue)}
.footer .links span{color:#444}
.footer .legal{margin-top:9px;color:#222}
.footer .legal a{color:var(--blue)}
.page--home .footer{top:390px}
.page--about .footer{top:514px}

.about__title{position:absolute;left:24px;top:121px;font-family:"Open Sans",sans-serif;font-weight:400;font-size:15px;letter-spacing:1px;color:var(--blue)}
.about__text{position:absolute;left:24px;top:157px;width:320px;font-size:6.7px;line-height:7.85px;letter-spacing:.3px;color:#222}
.about__text p+p{margin-top:7.8px}
.photo{position:absolute;left:353px;width:191px}
.photo--martini{top:118px;height:139px;background:linear-gradient(135deg,#3f6aa0,#8fb0cf 45%,#2f5584)}
.photo--bar{top:262px;height:97px;background:linear-gradient(120deg,#0e1630,#3a3258 40%,#8a5a3a 60%,#1c2340)}
</style>
</head>
<body>

<!-- Home page -->
<section class="page page--home">
  <div class="brand"><span class="brand__dot"></span>grain &amp; glint</div>
  <div class="social"><a><span class="social__box"></span>Chatter</a><a><span class="social__box"></span>Friendbook</a></div>
  <div class="contact"><b>t:</b> 020 7946 0321<br><b>e:</b> info@grainandglint.com</div>
  <ul class="nav">
    <li class="is-active" style="left:0">home<br>page</li>
    <li style="left:62px">grain<br>&amp; glint</li>
    <li style="left:155px">a little bit<br>about us</li>
    <li style="left:243px">our spirit<br>marketing</li>
    <li style="left:336px">big brand<br>success</li>
    <li style="left:426px">our<br>blog</li>
    <li style="left:480px">speak<br>to us</li>
    <span class="divider" style="left:46px"></span>
    <span class="divider" style="left:129px"></span>
    <span class="divider" style="left:225px"></span>
    <span class="divider" style="left:318px"></span>
    <span class="divider" style="left:410px"></span>
    <span class="divider" style="left:467px"></span>
    <div class="nav__bar"><span style="left:0;width:46px"></span></div>
  </ul>
  <div class="hero" role="img" aria-label="Close-up of bubbles rising in amber whisky">
    <blockquote class="hero__quote">
      <p>“turning our small<br>time whisky into a<br>national brand”</p>
      <cite>Tom Ashby<br>Veloria</cite>
    </blockquote>
  </div>
  <div class="features">
    <article class="card" style="left:9px"><h3>22 years experience<br>with big brands</h3><hr><p>Gismod, mauris vel biben du mfturingilla, fringilla, metutus dui vi fringilla, a artucu, vitae eleiffringilla.</p><a href="#"><svg viewBox="0 0 10 10"><circle cx="5" cy="5" r="4.3" fill="none" stroke="#1aa6d8"/><path d="M3 5h4M5.3 3.3 7 5 5.3 6.7" fill="none" stroke="#1aa6d8"/></svg><u>read more</u></a></article>
    <article class="card" style="left:180px"><h3>Making your drink<br>the next big brand</h3><hr><p>Gismod, mauris vel biben du mfturingilla, fringilla, metutus dui vi fringilla, a artucu, vitae eleiffringilla.</p><a href="#"><svg viewBox="0 0 10 10"><circle cx="5" cy="5" r="4.3" fill="none" stroke="#1aa6d8"/><path d="M3 5h4M5.3 3.3 7 5 5.3 6.7" fill="none" stroke="#1aa6d8"/></svg><u>read more</u></a></article>
    <article class="card" style="left:352px"><h3>350 outlets that<br>listen to what we say</h3><hr><p>Gismod, mauris vel biben du mfturingilla, fringilla, metutus dui vi fringilla, a artucu, vitae eleiffringilla.</p><a href="#"><svg viewBox="0 0 10 10"><circle cx="5" cy="5" r="4.3" fill="none" stroke="#1aa6d8"/><path d="M3 5h4M5.3 3.3 7 5 5.3 6.7" fill="none" stroke="#1aa6d8"/></svg><u>read more</u></a></article>
  </div>
  <footer class="footer">
    <div class="links">brand marketing <span>|</span> brand marketing strategy <span>|</span> drinks marketing <span>|</span> spirits marketing <span>|</span> alcoholic drinks marketing <span>|</span> drinks brand development</div>
    <div class="legal">© 1999-2010 Grain &amp; Glint &nbsp;| <a>terms and conditions</a> | <a>privacy policy</a></div>
  </footer>
</section>

<!-- About page -->
<section class="page page--about">
  <div class="brand"><span class="brand__dot"></span>grain &amp; glint</div>
  <div class="social"><a><span class="social__box"></span>Chatter</a><a><span class="social__box"></span>Friendbook</a></div>
  <div class="contact"><b>t:</b> 020 7946 0321<br><b>e:</b> info@grainandglint.com</div>
  <ul class="nav">
    <li style="left:0">home<br>page</li>
    <li class="is-active" style="left:62px">grain<br>&amp; glint</li>
    <li style="left:155px">a little bit<br>about us</li>
    <li style="left:243px">our spirit<br>marketing</li>
    <li style="left:336px">big brand<br>success</li>
    <li style="left:426px">our<br>blog</li>
    <li style="left:480px">speak<br>to us</li>
    <span class="divider" style="left:46px"></span>
    <span class="divider" style="left:129px"></span>
    <span class="divider" style="left:225px"></span>
    <span class="divider" style="left:318px"></span>
    <span class="divider" style="left:410px"></span>
    <span class="divider" style="left:467px"></span>
    <div class="nav__bar"><span style="left:46px;width:83px"></span></div>
  </ul>
  <h1 class="about__title">a little bit about us</h1>
  <div class="about__text">
    <p>Lorem ipsum dolor sit amet, consectetur adipiscing elit. Nulla cursus dignissim eleifend. Etiam suscipit urna non dui blandit molestie. Aliquam at felis a felis tincidunt tempor. In tempor, ipsum eu semper luctus, orci ipsum tempor libero, id vestibulum massa nunc in risus. Aliquam condimentum rhoncus vehicula. Ut tristique elementum sapien non accumsan. Nulla convallis elit quam, eu pellentesque risus. Suspendisse non nibh lorem. Nam porta tellus eu arcu tempus suscipit ultrices ligula ultricies. Aenean pretium accumsan aliquam. Nunc a enim felis, quis eleifend mi. In volutpat vulputate arcu, in lobortis nulla rutrum in. Integer a risus eu dolor faucibus hendrerit. Sed elementum, odio at placerat elementum, urna quam sagittis enim, sit amet blandit mi arcu et est. Nam congue blandit quam, at blandit arcu consectetur eu. Sed congue tristique augue, at pellentesque lectus mattis in. Mauris pulvinar tempus odio, id fringilla tortor blandit sed. Nam vel eros vel nibh dignissim hendrerit.</p>
    <p>Vivamus et adipiscing mauris. Praesent porttitor nisi sollicitudin purus pharetra eget ullamcorper nunc convallis. Maecenas porta luctus orci sed auctor. Donec sit amet est leo. Nam a ligula orci. Mauris at pulvinar mi. Praesent pretium nisi eu ligula faucibus dictum. Quisque commodo imperdiet elit, a vulputate sapien commodo at. Donec et dolor ut sapien posuere viverra. Vivamus euismod semper urna, viverra cursus odio mollis eu. Nam magna metus, aliquam eu pharetra vitae, blandit malesuada magna. Integer vitae diam ac augue rhoncus convallis. Nam id lacus sed mi ullamcorper venenatis quis sed ante. Morbi id ligula mi, sed porttitor ligula. Mauris hendrerit, ligula a aliquet vehicula, mi nulla tempus elit, vitae commodo leo dui a est. Aenean eu dui orci. Phasellus ullamcorper leo eget mauris ultrices hendrerit. Ut ultricies viverra diam, ut hendrerit nulla ultrices id.</p>
  </div>
  <div class="photo photo--martini" role="img" aria-label="Martini glass with an olive in cool blue light"></div>
  <div class="photo photo--bar" role="img" aria-label="Cocktail on a dimly lit bar counter with a crowd blurred behind"></div>
  <div class="features">
    <article class="card" style="left:9px"><h3>22 years experience<br>with big brands</h3><hr><p>Gismod, mauris vel biben du mfturingilla, fringilla, metutus dui vi fringilla, a artucu, vitae eleiffringilla.</p><a href="#"><svg viewBox="0 0 10 10"><circle cx="5" cy="5" r="4.3" fill="none" stroke="#1aa6d8"/><path d="M3 5h4M5.3 3.3 7 5 5.3 6.7" fill="none" stroke="#1aa6d8"/></svg><u>read more</u></a></article>
    <article class="card" style="left:180px"><h3>Making your drink<br>the next big brand</h3><hr><p>Gismod, mauris vel biben du mfturingilla, fringilla, metutus dui vi fringilla, a artucu, vitae eleiffringilla.</p><a href="#"><svg viewBox="0 0 10 10"><circle cx="5" cy="5" r="4.3" fill="none" stroke="#1aa6d8"/><path d="M3 5h4M5.3 3.3 7 5 5.3 6.7" fill="none" stroke="#1aa6d8"/></svg><u>read more</u></a></article>
    <article class="card" style="left:352px"><h3>350 outlets that<br>listen to what we say</h3><hr><p>Gismod, mauris vel biben du mfturingilla, fringilla, metutus dui vi fringilla, a artucu, vitae eleiffringilla.</p><a href="#"><svg viewBox="0 0 10 10"><circle cx="5" cy="5" r="4.3" fill="none" stroke="#1aa6d8"/><path d="M3 5h4M5.3 3.3 7 5 5.3 6.7" fill="none" stroke="#1aa6d8"/></svg><u>read more</u></a></article>
  </div>
  <footer class="footer">
    <div class="links">brand marketing <span>|</span> brand marketing strategy <span>|</span> drinks marketing <span>|</span> spirits marketing <span>|</span> alcoholic drinks marketing <span>|</span> drinks brand development</div>
    <div class="legal">© 1999-2010 Grain &amp; Glint &nbsp;| <a>terms and conditions</a> | <a>privacy policy</a></div>
  </footer>
</section>

</body>
</html>
```